Cellular Reward Program Flyer

We are launching a Customer Reward Program for our cellular retail business…. The marketing piece will be placed on our counter tops on high gloss cardstock or cardboard stand up type signs. I’m trying to keep this as clean and simple as possible. I found a few example’s of what I’d like to use as a basis.
Our biggest feature to our plan is our customers earn $20 every $100 spent. (requires 3 separate purchases)
No cards, no coupons, nothing needed.

our company logo is attached. you can also go to www.vontrelix.com for other info on the company as we are a franchise

Industry/Entity Type

Marketing

```html
<!DOCTYPE html>
<html lang="en">
<head>
<meta charset="utf-8">
<title>Vontrelix Reward Program Flyer</title>
<link href="https://fonts.googleapis.com/css2?family=Rokkitt:wght@400;500&family=Open+Sans:wght@300;400&display=swap" rel="stylesheet">
<style>
  :root {
    --backdrop: #1e1e1e;
    --paper: #ffffff;
    --ink: #1f1f1f;
    --accent: #f7941d;
    --rule: #b9b9b9;
    --muted: #3a3a3a;
    --wall-light: #f4f4f4;
    --wall-shade: #d9d9d9;
    --device-dark: #1a1a1a;
    --device-mid: #3b2418;
  }
  html, body {
    margin: 0;
    padding: 0;
    width: 1200px;
    height: 1000px;
    overflow: hidden;
    background: var(--backdrop);
  }
  .canvas {
    position: relative;
    width: 1200px;
    height: 1000px;
  }
  .flyer {
    position: absolute;
    left: 282px;
    top: 110px;
    width: 633px;
    height: 818px;
    background: var(--paper);
    overflow: hidden;
  }
  .hero {
    position: absolute;
    left: 0;
    top: 0;
    width: 633px;
    height: 400px;
  }
  .offer {
    position: absolute;
    left: 251px;
    top: 418px;
    width: 126px;
    display: flex;
    flex-direction: column;
    align-items: stretch;
    font-family: "Rokkitt", Georgia, serif;
    text-transform: uppercase;
    text-align: center;
  }
  .offer-word {
    color: var(--ink);
    font-weight: 500;
    font-size: 47px;
    line-height: 42px;
    height: 42px;
    letter-spacing: -1px;
    border-bottom: 1px dotted var(--rule);
  }
  .offer-amount {
    color: var(--accent);
    font-weight: 400;
    font-size: 74px;
    line-height: 66px;
    height: 66px;
    letter-spacing: -2px;
    border-bottom: 1px dotted var(--rule);
  }
  .offer > :last-child { border-bottom: none; }
  .footer-curves {
    position: absolute;
    left: 0;
    top: 700px;
    width: 633px;
    height: 118px;
  }
  .brand {
    position: absolute;
    left: 24px;
    top: 752px;
    display: flex;
    align-items: center;
    gap: 8px;
  }
  .brand-dot {
    width: 22px;
    height: 22px;
    border-radius: 50%;
    background: var(--accent);
  }
  .brand-name {
    font-family: "Rokkitt", Georgia, serif;
    font-weight: 400;
    font-size: 30px;
    color: var(--muted);
    line-height: 1;
  }
  .contact {
    position: absolute;
    right: 18px;
    top: 757px;
    text-align: right;
    font-family: "Open Sans", Arial, sans-serif;
  }
  .contact-phone {
    color: var(--accent);
    font-weight: 300;
    font-size: 17px;
    line-height: 22px;
    padding-bottom: 2px;
    border-bottom: 1px dotted var(--rule);
  }
  .contact-hours {
    color: var(--muted);
    font-weight: 400;
    font-size: 10px;
    letter-spacing: 3px;
    margin-top: 4px;
    margin-right: -3px;
  }
</style>
</head>
<body>
<div class="canvas">
  <main class="flyer">
    <svg class="hero" viewBox="0 0 633 400" role="img" aria-label="Photo of three smartphones against a white brick wall, showing shopping basket, wallet with dollar signs and refresh icons on their screens">
      <defs>
        <linearGradient id="wall" x1="0" y1="0" x2="0" y2="1">
          <stop offset="0" stop-color="var(--wall-light)"/>
          <stop offset="0.55" stop-color="var(--wall-shade)" stop-opacity="0.5"/>
          <stop offset="1" stop-color="var(--paper)"/>
        </linearGradient>
        <linearGradient id="devices" x1="0" y1="0" x2="1" y2="0">
          <stop offset="0" stop-color="var(--device-dark)"/>
          <stop offset="0.5" stop-color="var(--device-mid)"/>
          <stop offset="1" stop-color="var(--device-dark)"/>
        </linearGradient>
      </defs>
      <rect x="0" y="0" width="633" height="400" fill="url(#wall)"/>
      <rect x="120" y="36" width="390" height="344" rx="14" fill="url(#devices)"/>
    </svg>

    <section class="offer" aria-label="Reward offer">
      <div class="offer-word">Earn</div>
      <div class="offer-amount">$20</div>
      <div class="offer-word">Every</div>
      <div class="offer-amount">$100</div>
      <div class="offer-word">Spent</div>
    </section>

    <svg class="footer-curves" viewBox="0 0 633 118" aria-hidden="true">
      <path d="M0 23 Q 230 -5 440 118" fill="none" stroke="var(--rule)" stroke-width="1" stroke-dasharray="4 3"/>
      <path d="M373 85 Q 500 20 633 13" fill="none" stroke="var(--rule)" stroke-width="1" stroke-dasharray="4 3"/>
    </svg>

    <div class="brand">
      <span class="brand-dot"></span>
      <span class="brand-name">Vontrelix</span>
    </div>

    <div class="contact">
      <div class="contact-phone">555.014.2090, X2</div>
      <div class="contact-hours">M-F, 9:30-6 (EST)</div>
    </div>
  </main>
</div>
</body>
</html>
```